Boldmere Nutrition: Premium Sports Nutrition (Package Design)

We are a Premium Sports Nutrition Company, looking at nutrition needs of outdoor athletes in focus.
We Need Packaging for our Protein Product, called 1. Protein: Recovery
Flavour: Mild Chocolate
and 2. Vimtrax: Summit

The Packaging should be Premium, Should look like an upmarket product
but should not look as an artificial or synthetic product.
Should look like a consumable product which people will consume and looks safe to consume.
At the same time, should look very eye catching and get attention of the people.
User Friendly Yet Premium and Elegant Design.

We would like to go for a single colour as Base.
The Logo should Sync in well with the package.
The content text should be simple not much bold.

The design can include sports icon, including Cycling,Swimming,Running,Gymming,Hockey as a must if applied.
These should be placed on the top of the packaging

This packaging is required for sachets and cardboard boxes, plastic boxes, thus designers are required to send all three.

Sachets are expected to be 170mm tall and 108mm wide, single serve stand up sachet pouch.

All designers to send packaging of all of these in
1. Sachet Base Colour (1. Matte White 2. Matte Black)
2. Plastic Boxes
3. Cardboard Box to keep the sachets in it
Updates

We are still looking for more options!

Target Market(s)

Sports Nutrition, Gym Goers, Outdoor Athletes, Cyclists, Runners, Triathletes, Swimmers, Hockey, Cricket Players

Industry/Entity Type

Nutrition

Font styles to use
Sans Serif

Requirements
Must have
• Sync in well with the Logo
• Should Blend well with Matte White Colour as Base of the Sachet

```html
<!DOCTYPE html>
<html lang="en">
<head>
<meta charset="utf-8">
<title>Boldmere Nutrition – Protein Recovery Sachet Label</title>
<link rel="stylesheet" href="https://fonts.googleapis.com/css2?family=Montserrat:wght@600;700&family=Oswald:wght@600&family=Graduate&display=swap">
<style>
  :root {
    --page-bg: #f4f5f6;
    --label-white: #ffffff;
    --navy: #15486f;
    --blue: #1f6a9a;
    --blue-light: #2f86b8;
    --green: #5fae2e;
    --green-light: #9ccf3a;
    --lime: #d7ea55;
    --grey-text: #f2f2f2;
  }
  html, body {
    margin: 0;
    width: 1200px;
    height: 842px;
    overflow: hidden;
    background: var(--page-bg);
  }
  .sachet-label {
    position: absolute;
    left: 330px;
    top: 36px;
    width: 540px;
    height: 770px;
    background: var(--label-white);
    box-shadow: 0 4px 18px rgba(0,0,0,0.12);
    overflow: hidden;
  }
  .label-art {
    position: absolute;
    inset: 0;
  }
  .sport-icons {
    position: absolute;
    top: 70px;
    left: 50%;
    transform: translateX(-50%);
    display: flex;
    gap: 6px;
  }
  .sport-icon {
    width: 50px;
    height: 50px;
    background: var(--blue);
    border: 2px solid var(--label-white);
    box-sizing: border-box;
  }
  .brand {
    position: absolute;
    top: 168px;
    left: 0;
    right: 0;
    text-align: center;
  }
  .brand-name {
    display: inline-flex;
    align-items: center;
    gap: 10px;
    font-family: "Montserrat", sans-serif;
    font-weight: 700;
    font-size: 27px;
    color: var(--navy);
    border-bottom: 1.5px solid var(--green);
    padding-bottom: 4px;
  }
  .brand-dot {
    width: 18px;
    height: 18px;
    border-radius: 50%;
    background: var(--green);
  }
  .brand-tagline {
    margin-top: 5px;
    font-family: "Montserrat", sans-serif;
    font-weight: 600;
    font-size: 9px;
    letter-spacing: 2.5px;
    color: var(--navy);
  }
  .product-title {
    position: absolute;
    top: 300px;
    left: 0;
    right: 0;
    text-align: center;
    color: var(--navy);
  }
  .product-kicker {
    font-family: "Montserrat", sans-serif;
    font-weight: 700;
    font-size: 34px;
    letter-spacing: 0.5px;
    margin: 0;
  }
  .product-name {
    font-family: "Oswald", sans-serif;
    font-weight: 600;
    font-size: 74px;
    line-height: 1;
    margin: 6px 0 0;
    transform: scaleY(1.12);
  }
  .product-flavour {
    font-family: "Graduate", serif;
    font-size: 33px;
    letter-spacing: 2px;
    margin: 14px 0 0;
  }
  .net-weight {
    position: absolute;
    bottom: 30px;
    left: 0;
    right: 0;
    text-align: center;
    font-family: "Montserrat", sans-serif;
    font-weight: 600;
    font-size: 14px;
    color: var(--grey-text);
  }
</style>
</head>
<body>
  <div class="sachet-label">
    <svg class="label-art" viewBox="0 0 540 770" aria-hidden="true">
      <defs>
        <linearGradient id="band-blue" x1="0" y1="0" x2="1" y2="0">
          <stop offset="0" stop-color="#15486f"/>
          <stop offset="0.5" stop-color="#2f86b8"/>
          <stop offset="1" stop-color="#15486f"/>
        </linearGradient>
        <linearGradient id="wave-green" x1="0" y1="0" x2="1" y2="0">
          <stop offset="0" stop-color="#4f9f28"/>
          <stop offset="0.6" stop-color="#8cc63a"/>
          <stop offset="1" stop-color="#d7ea55"/>
        </linearGradient>
      </defs>
      <!-- top band with central tab -->
      <path d="M0 0 H540 V105 Q470 70 400 72 L140 72 Q70 70 0 105 Z" fill="url(#band-blue)"/>
      <rect x="140" y="60" width="260" height="72" rx="14" fill="#1b5a86"/>
      <!-- bottom wave -->
      <path d="M0 640 Q150 560 300 610 T540 560 V770 H0 Z" fill="#c9ced2"/>
      <path d="M0 655 Q150 580 300 628 T540 580 V770 H0 Z" fill="#ffffff"/>
      <path d="M0 668 Q150 600 300 645 T540 600 V770 H0 Z" fill="url(#wave-green)"/>
    </svg>

    <div class="sport-icons">
      <div class="sport-icon" role="img" aria-label="Cycling pictogram"></div>
      <div class="sport-icon" role="img" aria-label="Swimming pictogram"></div>
      <div class="sport-icon" role="img" aria-label="Weightlifting pictogram"></div>
      <div class="sport-icon" role="img" aria-label="Hockey pictogram"></div>
    </div>

    <div class="brand">
      <div class="brand-name"><span class="brand-dot"></span>Boldmere Nutrition</div>
      <div class="brand-tagline">PREMIUM SPORTS NUTRITION</div>
    </div>

    <div class="product-title">
      <p class="product-kicker">100% PROTEIN</p>
      <h1 class="product-name">RECOVERY FLAVOUR</h1>
      <p class="product-flavour">MILD CHOCOLATE</p>
    </div>

    <div class="net-weight">NET WT. 908 g(2lb)</div>
  </div>
</body>
</html>
```